Marta Quinlan Photography needs a unique, creative business card/logo design

I need a design for business cards/logo that is unique and creative in the industry. Simplicity is nice, so not too crowded. Something that will catch my customer's eye and remain in their memory. I am primarily a landscape photographer but will be soon may be branching into boudoir photography as well. I have attached my current card.

Industry/Entity Type

Business

Contact Information for Business Card

Marta Quinlan Photography
Phone: 0439 271 504
Email: MartaQuinlanPhotography@brivomail.net
Website: www.pagerly.net/MartaQuinlanPhotography.Aust

Logo Text

Marta Quinlan Photography

Requirements
Must have
• Contact Details on one side
Should not have
• pixelation

```html
<!DOCTYPE html>
<html lang="en">
<head>
<meta charset="utf-8">
<title>Marta Quinlan Photography – Business Card</title>
<link rel="stylesheet" href="https://fonts.googleapis.com/css2?family=Lato:wght@400;700&display=swap">
<style>
  :root {
    --backdrop: #e9e6e2;
    --card: #232323;
    --card-edge: #1b1b1b;
    --ink-bright: #f2f2f2;
    --ink-mid: #bdbdbd;
    --ink-soft: #8a8a8a;
    --ring-faint: #3a3a3a;
    --rule: #9a9a9a;
  }
  * { box-sizing: border-box; margin: 0; padding: 0; }
  html, body {
    width: 1200px;
    height: 1000px;
    overflow: hidden;
    background: var(--backdrop);
    font-family: "Lato", Arial, sans-serif;
  }
  .canvas {
    position: relative;
    width: 1200px;
    height: 1000px;
  }
  .card {
    position: absolute;
    width: 600px;
    height: 350px;
    background: var(--card);
    border: 1px solid var(--card-edge);
    box-shadow: 0 6px 18px rgba(0, 0, 0, 0.22);
    overflow: hidden;
  }

  /* Logo side */
  .card--brand {
    left: 470px;
    top: 90px;
    display: flex;
    align-items: center;
    justify-content: center;
  }
  .brand-lockup {
    display: flex;
    align-items: center;
    gap: 14px;
  }
  .brand-dot {
    width: 14px;
    height: 14px;
    border-radius: 50%;
    background: var(--ink-mid);
  }
  .brand-name {
    font-size: 30px;
    font-weight: 700;
    letter-spacing: 2px;
    color: var(--ink-mid);
  }

  /* Contact side */
  .card--contact {
    left: 130px;
    top: 530px;
  }
  .faint-ring {
    position: absolute;
    left: 34px;
    top: 26px;
  }
  .contact-block {
    position: absolute;
    left: 180px;
    top: 150px;
    color: var(--ink-bright);
  }
  .wordmark {
    font-size: 24px;
    font-weight: 700;
    letter-spacing: 1.5px;
    color: var(--ink-bright);
    line-height: 1.1;
  }
  .wordmark-rule {
    width: 80px;
    height: 1px;
    margin: 12px 0 12px;
    background: linear-gradient(90deg, var(--rule), transparent);
  }
  .person-name {
    font-size: 17px;
    font-weight: 700;
    color: var(--ink-mid);
    margin-bottom: 12px;
  }
  .contact-list {
    list-style: none;
    font-size: 15px;
    line-height: 23px;
    color: var(--ink-bright);
  }
  .contact-list li {
    display: flex;
    align-items: center;
    gap: 8px;
  }
  .contact-icon {
    width: 11px;
    height: 11px;
    flex: none;
  }
  .contact-list .fade { color: var(--ink-soft); }
</style>
</head>
<body>
<main class="canvas">

  <section class="card card--brand" aria-label="Business card, logo side">
    <div class="brand-lockup">
      <span class="brand-dot"></span>
      <span class="brand-name">Marta Quinlan</span>
    </div>
  </section>

  <section class="card card--contact" aria-label="Business card, contact side">
    <svg class="faint-ring" width="170" height="170" viewBox="0 0 170 170" aria-hidden="true">
      <circle cx="85" cy="85" r="80" fill="none" stroke="var(--ring-faint)" stroke-width="3"/>
    </svg>

    <div class="contact-block">
      <p class="wordmark">Marta Quinlan Photography</p>
      <div class="wordmark-rule"></div>
      <p class="person-name">Marta Quinlan</p>
      <ul class="contact-list">
        <li>
          <svg class="contact-icon" viewBox="0 0 12 12" aria-hidden="true">
            <rect x="3" y="0.5" width="6" height="11" rx="1.2" fill="none" stroke="currentColor" stroke-width="1.2"/>
            <circle cx="6" cy="9.4" r="0.7" fill="currentColor"/>
          </svg>
          <span>0439 271 504</span>
        </li>
        <li>
          <svg class="contact-icon" viewBox="0 0 12 12" aria-hidden="true">
            <rect x="0.5" y="2.5" width="11" height="7" fill="currentColor"/>
            <path d="M0.8 2.8 L6 6.8 L11.2 2.8" fill="none" stroke="var(--card)" stroke-width="1"/>
          </svg>
          <span>MartaQuinlanPhotography@brivomail.net</span>
        </li>
        <li>
          <svg class="contact-icon" viewBox="0 0 12 12" aria-hidden="true">
            <circle cx="6" cy="6" r="3" fill="currentColor"/>
          </svg>
          <span>MartaQuinlanPhotography.Aust</span>
        </li>
      </ul>
    </div>
  </section>

</main>
</body>
</html>
```